Business Card Design Project

We have a logo design and are now looking for a business card design. We supply pre-construction services to the Wireless Telecommunication Industry in the development of cell phone tower and other antenna supporting infrastructure e.g. buildings. The types of services include Real Estate Leasing, Zoning & Permitting,Surveying and A&E work. I am looking for a card that includes the logo we have selected along with the full company name. Company colors are Blue and Silver. I want something professional and that "pops". Use your imagination with the four sided star portion of the logo - it can be stretched such that it occupies a large portion of the card or kept simple the way it is. I am interested in seeing the design on a white, silver, navy, black or charcoal background or any other color you think works well with the logo. Apart from the logo that includes HRM we also need to see the full company name on the card - Harborline Relay Maintenance, Inc. The design must also show a persons name, title, address, (2) phone numbers, e-mail address and web address www.hrm.example

Target Market(s)

Cell phone carriers e.g. Quellport Mobile, BN&K, Zandex Cell, Ovalo etc.

Industry/Entity Type

Cell Phone

Requirements
Must have
• Logo and
Harborline Relay Maintenance, Inc.

```html
<!DOCTYPE html>
<html lang="en">
<head>
<meta charset="utf-8">
<title>HRM Business Card</title>
<link href="https://fonts.googleapis.com/css2?family=Open+Sans:wght@400;600;700&display=swap" rel="stylesheet">
<style>
  :root {
    --backdrop: #d9d9d9;
    --card: #ffffff;
    --brand-blue: #2e86d1;
    --brand-deep: #1a6fc0;
    --brand-light: #6fb4ea;
    --ink: #333333;
    --rule: #7a7a7a;
    --silver: #8c97a3;
  }
  * { margin: 0; padding: 0; box-sizing: border-box; }
  html, body {
    width: 1200px;
    height: 787px;
    overflow: hidden;
    background: var(--backdrop);
    font-family: "Open Sans", Arial, sans-serif;
  }
  .business-card {
    position: absolute;
    left: 180px;
    top: 153px;
    width: 840px;
    height: 480px;
    background: var(--card);
    overflow: hidden;
    box-shadow: 0 12px 30px rgba(0,0,0,0.18);
  }
  .corner-band {
    position: absolute;
    top: 0;
    right: 0;
    width: 840px;
    height: 480px;
  }
  .brand {
    position: absolute;
    left: 52px;
    top: 40px;
    display: flex;
    flex-direction: column;
  }
  .brand-mark {
    display: flex;
    align-items: center;
    gap: 12px;
  }
  .brand-dot {
    width: 26px;
    height: 26px;
    border-radius: 50%;
    background: var(--brand-blue);
  }
  .brand-name {
    font-size: 44px;
    font-weight: 700;
    color: var(--brand-blue);
    line-height: 1;
    letter-spacing: 1px;
  }
  .brand-full {
    margin-top: 6px;
    margin-left: 38px;
    font-size: 9px;
    font-weight: 600;
    color: var(--silver);
    text-transform: uppercase;
    letter-spacing: 0.6px;
  }
  .person {
    position: absolute;
    left: 232px;
    width: 460px;
    top: 160px;
    text-align: center;
    color: var(--brand-blue);
  }
  .person-name {
    font-size: 42px;
    font-weight: 600;
    letter-spacing: 2px;
    line-height: 1.1;
  }
  .person-title {
    font-size: 22px;
    font-weight: 600;
    letter-spacing: 1px;
  }
  .divider {
    position: absolute;
    left: 297px;
    top: 300px;
    width: 330px;
    height: 2px;
    background: var(--rule);
  }
  .contact {
    position: absolute;
    left: 232px;
    width: 460px;
    top: 318px;
    text-align: center;
    list-style: none;
    color: var(--ink);
    font-size: 14px;
    font-weight: 700;
    line-height: 1.55;
    text-transform: uppercase;
  }
</style>
</head>
<body>
  <article class="business-card">
    <svg class="corner-band" viewBox="0 0 840 480" role="img" aria-label="Large blue star-point decoration in the corners">
      <defs>
        <linearGradient id="bandGradient" x1="0" y1="0" x2="1" y2="1">
          <stop offset="0" stop-color="#6fb4ea"/>
          <stop offset="1" stop-color="#1a6fc0"/>
        </linearGradient>
      </defs>
      <polygon points="500,0 840,0 840,320" fill="url(#bandGradient)"/>
      <polygon points="0,340 0,480 80,480" fill="url(#bandGradient)"/>
    </svg>

    <header class="brand">
      <div class="brand-mark">
        <span class="brand-dot"></span>
        <span class="brand-name">HRM</span>
      </div>
      <span class="brand-full">Harborline Relay Maintenance, Inc.</span>
    </header>

    <section class="person">
      <h1 class="person-name">JOHN KNOW</h1>
      <p class="person-title">TITLE HERE</p>
    </section>

    <div class="divider"></div>

    <ul class="contact">
      <li>Address: Address goes here</li>
      <li>Phone numbers: 001122334455</li>
      <li>E-mail: johnknow@hrm.example</li>
      <li>Web address: www.hrm.example</li>
    </ul>
  </article>
</body>
</html>
```